Project Halcyon PowerPoint Design

This is a PPT design for Power & Utilities company who are in the process of a technology upgrade for their Finance department. We are looking to develop a branded PPT for Project Halcyon (specifically HALCYON). Why does Halcyon resonate? "The Earth is pointed almost directly at Halcyon. During the course of the night,
Halcyon does not rise or set, but remains in nearly the same spot above the
northern horizon year- round while the other stars circle around it."
Halcyon represents the guiding principles that manage, monitor and
control the organizations financials.

Target Market(s)

Finance stakeholders impacted by technology enhancement

Font styles to use
Serif
Other font styles liked:
• Arial

Colors
0054AA
0677BA
7BADD7
CADEEF
E8F1F8

Requirements
Must have
• Various slide layout ( Cover slide, content slide, divider, etc). Attached is the logo and corporate colors
Nice to have
• Over the top creativity

```html
<!DOCTYPE html>
<html lang="en">
<head>
<meta charset="utf-8">
<title>Project Halcyon – Presentation Template</title>
<link rel="stylesheet" href="https://fonts.googleapis.com/css2?family=Montserrat:wght@400;500;600&display=swap">
<style>
:root{
  --navy:#0054AA;
  --ocean:#0677BA;
  --sky:#7BADD7;
  --mist:#CADEEF;
  --ice:#E8F1F8;
  --ink:#111111;
  --stage:#ececee;
  --board:#d6d6d9;
  --white:#ffffff;
}
*{box-sizing:border-box;margin:0;padding:0}
html,body{width:1200px;height:3161px;overflow:hidden}
body{font-family:"Montserrat",Arial,sans-serif;color:var(--ink);background:var(--board);position:relative}
.hero{position:absolute;left:0;top:0;width:1200px;height:860px;background:linear-gradient(#f3f3f5,#e4e4e7)}
.hero-slide{position:absolute;left:220px;top:210px;transform:scale(1.4074);transform-origin:0 0;box-shadow:0 10px 30px rgba(0,0,0,.18)}
.slide{position:absolute;width:540px;height:302px;overflow:hidden;background:var(--white)}
.slide>*{position:absolute}
.defs{position:absolute;width:0;height:0}

/* cover */
.cover .art{left:0;top:0;width:540px;height:282px}
.cover .brand{left:46px;top:44px}
.brand{font-weight:500;color:var(--navy);line-height:1}
.brand-sup{display:block;font-size:9px;letter-spacing:3px;margin-left:34px}
.brand-name{display:block;font-size:26px;letter-spacing:2px}
.brand-dot{display:inline-block;width:7px;height:7px;border-radius:50%;background:currentColor;margin-right:6px;vertical-align:middle}
.cover .title{left:46px;top:112px;font-size:27px;font-weight:600;line-height:1.12;color:var(--white)}
.cover .subtitle{left:46px;top:180px;font-size:10.5px;color:var(--navy)}
.cover .date{left:46px;top:220px;width:145px;height:16px;border-radius:3px;background:var(--navy);color:var(--white);font-size:7px;display:flex;align-items:center;justify-content:center;box-shadow:2px 2px 0 rgba(0,0,0,.25)}
.cover .foot{left:0;bottom:0;width:540px;height:20px;font-size:6px;display:flex;align-items:center;justify-content:center;background:var(--white);color:#333}
.foot b{font-weight:500;color:var(--navy)}
.cover--sky{background:var(--sky)}
.cover--white .title,.cover--white .subtitle{}
.cover--white .title{color:var(--ink)}
.cover--white .foot{background:var(--sky);color:var(--white)}
.cover--black{background:var(--ink)}
.cover--black .brand{color:var(--white)}
.cover--black .subtitle{color:var(--navy)}
.cover--black .date{background:var(--mist);color:var(--navy)}

/* content slides */
.slide-title{left:0;width:100%;text-align:center;font-size:19px;font-weight:500;top:24px}
.slide-sub{left:0;width:100%;text-align:center;font-size:9.5px;color:var(--ocean);top:50px}
.footer-bar{left:0;bottom:0;width:540px;height:30px}
.footer-brand{left:12px;bottom:5px;font-size:12px;font-weight:500;color:var(--navy);letter-spacing:1px}
.lorem{font-size:6.5px;line-height:1.3;color:#444}
.h-blue{font-size:12px;color:var(--ocean);font-weight:500}
.photo{border-radius:0}

.toc-item{width:200px;display:flex;gap:8px}
.toc-num{font-size:19px;color:#bbb;width:18px;text-align:right;padding-right:6px;border-right:1px solid #ccc;height:32px;line-height:32px}
.toc-body .h-blue{font-size:12px}

ul.bul{list-style:none}
ul.bul li{position:relative;padding-left:9px;margin-bottom:5px}
ul.bul li::before{content:"";position:absolute;left:1px;top:3px;width:3px;height:3px;border-radius:50%;background:var(--ocean)}

table.grid{border-collapse:collapse;font-size:6.5px;width:480px}
table.grid th{background:var(--sky);color:var(--white);font-weight:400;height:22px;border-right:2px solid var(--white)}
table.grid th:first-child{background:var(--navy);text-align:left;padding-left:4px;font-weight:600}
table.grid td{height:17px;text-align:center;background:#f6f6f7;border-bottom:1px solid #e3e3e5}
table.grid td:first-child{text-align:left;padding-left:4px}

.legend .h-blue{font-size:10px}
.legend-row{width:170px}
.legend-sw{position:absolute;left:-16px;top:2px;width:10px;height:10px}
</style>
</head>
<body>

<svg class="defs" aria-hidden="true">
  <defs>
    <linearGradient id="g-desk" x1="0" y1="0" x2="1" y2="1"><stop offset="0" stop-color="#8a6b4c"/><stop offset=".5" stop-color="#d2b18a"/><stop offset="1" stop-color="#ece0cf"/></linearGradient>
    <linearGradient id="g-hands" x1="0" y1="0" x2="1" y2="1"><stop offset="0" stop-color="#8fa0b3"/><stop offset=".5" stop-color="#3b4f66"/><stop offset="1" stop-color="#1d2835"/></linearGradient>
    <linearGradient id="g-docs" x1="0" y1="0" x2="1" y2="1"><stop offset="0" stop-color="#4a3a30"/><stop offset=".5" stop-color="#c9b8a8"/><stop offset="1" stop-color="#eeeae6"/></linearGradient>
    <linearGradient id="g-chart" x1="0" y1="0" x2="1" y2="1"><stop offset="0" stop-color="#eef0f4"/><stop offset="1" stop-color="#b9c4d6"/></linearGradient>
    <linearGradient id="g-tablet" x1="0" y1="0" x2="1" y2="1"><stop offset="0" stop-color="#c9cfd6"/><stop offset="1" stop-color="#4f5b66"/></linearGradient>
    <linearGradient id="g-sectionbg" x1="0" y1="0" x2="1" y2="1"><stop offset="0" stop-color="#8db7dc"/><stop offset="1" stop-color="#6fa2cf"/></linearGradient>
    <linearGradient id="g-dark" x1="0" y1="0" x2="1" y2="1"><stop offset="0" stop-color="#0c0c0c"/><stop offset="1" stop-color="#2a2d33"/></linearGradient>
  </defs>
</svg>

<section class="hero">
  <div class="slide cover cover--sky hero-slide">
    <svg class="art" viewBox="0 0 540 282"><circle cx="500" cy="120" r="182" fill="var(--navy)"/><circle cx="536" cy="110" r="168" fill="url(#g-desk)" role="img" aria-label="Photo of coffee mug and tablet with charts on a desk"/></svg>
    <div class="brand"><span class="brand-sup">PROJECT</span><span class="brand-name"><span class="brand-dot"></span>HALCYON</span></div>
    <div class="title">Presentation<br>Title Goes Here!</div>
    <div class="subtitle">Subtitle of Presentation Goes Here!</div>
    <div class="date">Thursday, November 11, 2021</div>
    <div class="foot">© 2020&nbsp;<b>Project-Halcyon</b>&nbsp;| All Rights Reserved.</div>
  </div>
</section>

<!-- row 1 -->
<div class="slide cover cover--sky" style="left:50px;top:868px">
  <svg class="art" viewBox="0 0 540 282"><circle cx="500" cy="120" r="182" fill="var(--navy)"/><circle cx="536" cy="110" r="168" fill="url(#g-desk)" role="img" aria-label="Photo of coffee mug and tablet with charts on a desk"/></svg>
  <div class="brand"><span class="brand-sup">PROJECT</span><span class="brand-name"><span class="brand-dot"></span>HALCYON</span></div>
  <div class="title">Presentation<br>Title Goes Here!</div>
  <div class="subtitle">Subtitle of Presentation Goes Here!</div>
  <div class="date">Thursday, November 11, 2021</div>
  <div class="foot">© 2020&nbsp;<b>Project-Halcyon</b>&nbsp;| All Rights Reserved.</div>
</div>
<div class="slide cover cover--white" style="left:609px;top:868px">
  <svg class="art" viewBox="0 0 540 282"><circle cx="500" cy="120" r="182" fill="var(--navy)"/><circle cx="536" cy="110" r="168" fill="url(#g-hands)" role="img" aria-label="Photo of business handshake"/></svg>
  <div class="brand"><span class="brand-sup">PROJECT</span><span class="brand-name"><span class="brand-dot"></span>HALCYON</span></div>
  <div class="title">Presentation<br>Title Goes Here!</div>
  <div class="subtitle">Subtitle of Presentation Goes Here!</div>
  <div class="date">Thursday, November 11, 2021</div>
  <div class="foot">© 2020&nbsp;<b>Project-Halcyon</b>&nbsp;| All Rights Reserved.</div>
</div>

<!-- row 2 -->
<div class="slide cover cover--black" style="left:50px;top:1189px">
  <svg class="art" viewBox="0 0 540 282"><circle cx="500" cy="120" r="182" fill="var(--navy)"/><circle cx="536" cy="110" r="168" fill="url(#g-docs)" role="img" aria-label="Photo of hands reviewing a signed document"/></svg>
  <div class="brand"><span class="brand-sup">PROJECT</span><span class="brand-name"><span class="brand-dot"></span>HALCYON</span></div>
  <div class="title">Presentation<br>Title Goes Here!</div>
  <div class="subtitle">Subtitle of Presentation Goes Here!</div>
  <div class="date">Thursday, November 11, 2021</div>
  <div class="foot">© 2020&nbsp;<b>Project-Halcyon</b>&nbsp;| All Rights Reserved.</div>
</div>
<div class="slide cover cover--sky" style="left:609px;top:1189px">
  <svg class="art" viewBox="0 0 540 282"><circle cx="510" cy="120" r="176" fill="var(--navy)"/><circle cx="546" cy="110" r="162" fill="url(#g-desk)" role="img" aria-label="Photo of coffee mug and tablet with charts on a desk"/></svg>
  <div class="brand"><span class="brand-sup">PROJECT</span><span class="brand-name"><span class="brand-dot"></span>HALCYON</span></div>
  <div class="title">Presentation<br>Title Goes Here!</div>
  <div class="subtitle">Subtitle of Presentation Goes Here!</div>
  <div class="date">Thursday, November 11, 2021</div>
  <div class="foot">© 2020&nbsp;<b>Project-Halcyon</b>&nbsp;| All Rights Reserved.</div>
</div>

<!-- row 3 -->
<div class="slide cover cover--white" style="left:50px;top:1510px">
  <svg class="art" viewBox="0 0 540 282"><circle cx="510" cy="120" r="176" fill="var(--navy)"/><circle cx="546" cy="110" r="162" fill="url(#g-hands)" role="img" aria-label="Photo of business handshake"/></svg>
  <div class="brand"><span class="brand-sup">PROJECT</span><span class="brand-name"><span class="brand-dot"></span>HALCYON</span></div>
  <div class="title">Presentation<br>Title Goes Here!</div>
  <div class="subtitle">Subtitle of Presentation Goes Here!</div>
  <div class="date">Thursday, November 11, 2021</div>
  <div class="foot">© 2020&nbsp;<b>Project-Halcyon</b>&nbsp;| All Rights Reserved.</div>
</div>
<div class="slide cover cover--black" style="left:609px;top:1510px">
  <svg class="art" viewBox="0 0 540 282"><circle cx="510" cy="120" r="176" fill="var(--navy)"/><circle cx="546" cy="110" r="162" fill="url(#g-docs)" role="img" aria-label="Photo of hands reviewing a signed document"/></svg>
  <div class="brand"><span class="brand-sup">PROJECT</span><span class="brand-name"><span class="brand-dot"></span>HALCYON</span></div>
  <div class="title">Presentation<br>Title Goes Here!</div>
  <div class="subtitle">Subtitle of Presentation Goes Here!</div>
  <div class="date">Thursday, November 11, 2021</div>
  <div class="foot">© 2020&nbsp;<b>Project-Halcyon</b>&nbsp;| All Rights Reserved.</div>
</div>

<!-- row 4: table of contents -->
<div class="slide" style="left:50px;top:1832px">
  <div class="slide-title">Table of Contents</div>
  <div class="slide-sub">Slide subtitle Goes Here</div>
  <div class="toc-item" style="left:70px;top:98px"><div class="toc-num">1</div><div class="toc-body"><div class="h-blue">Title Goes Here</div><div class="lorem">Lorem ipsum dolor sit amet, consectetur adipiscing elit. Vivamus eu dui ex.</div></div></div>
  <div class="toc-item" style="left:283px;top:98px"><div class="toc-num">2</div><div class="toc-body"><div class="h-blue">Title Goes Here</div><div class="lorem">Lorem ipsum dolor sit amet, consectetur adipiscing elit. Vivamus eu dui ex.</div></div></div>
  <div class="toc-item" style="left:70px;top:151px"><div class="toc-num">3</div><div class="toc-body"><div class="h-blue">Title Goes Here</div><div class="lorem">Lorem ipsum dolor sit amet, consectetur adipiscing elit. Vivamus eu dui ex.</div></div></div>
  <div class="toc-item" style="left:283px;top:151px"><div class="toc-num">4</div><div class="toc-body"><div class="h-blue">Title Goes Here</div><div class="lorem">Lorem ipsum dolor sit amet, consectetur adipiscing elit. Vivamus eu dui ex.</div></div></div>
  <div class="toc-item" style="left:70px;top:204px"><div class="toc-num">5</div><div class="toc-body"><div class="h-blue">Title Goes Here</div><div class="lorem">Lorem ipsum dolor sit amet, consectetur adipiscing elit. Vivamus eu dui ex.</div></div></div>
  <div class="toc-item" style="left:283px;top:204px"><div class="toc-num">6</div><div class="toc-body"><div class="h-blue">Title Goes Here</div><div class="lorem">Lorem ipsum dolor sit amet, consectetur adipiscing elit. Vivamus eu dui ex.</div></div></div>
  <svg class="footer-bar" viewBox="0 0 540 30"><rect x="0" y="26" width="540" height="4" fill="var(--sky)"/><polygon points="0,8 82,8 100,26 0,26" fill="var(--mist)"/><line x1="92" y1="18" x2="520" y2="18" stroke="var(--navy)" stroke-width="1.5"/><circle cx="520" cy="18" r="6" fill="var(--navy)"/><text x="520" y="20.5" font-size="6" fill="#fff" text-anchor="middle" font-family="Montserrat, Arial, sans-serif">2</text></svg>
  <div class="footer-brand">HALCYON</div>
</div>
<div class="slide" style="left:609px;top:1832px">
  <div role="img" aria-label="Photo of hand with pen over printed financial charts" style="left:23px;top:22px;width:265px;height:235px;background:linear-gradient(135deg,#f1f3f6,#b8c3d4)"></div>
  <div style="left:300px;top:58px;width:220px;text-align:center;font-size:17px;font-weight:500;line-height:1.15">Slide Title<br>Goes Here</div>
  <div class="lorem" style="left:310px;top:112px;width:200px;text-align:center;font-size:7px">Lorem ipsum dolor sit amet, consectetur adipiscing elit. Vivamus eu dui ex. Curabitur dapibus dignissim dui, in molestie metus feugiat sed. Praesent aliquet lorem ex, eu dapibus odio varius at. Duis eget tellus porta, consequat lacus vitae, venenatis dolor. Nulla facilisi. In et sollicitudin lacus. Donec risus orci, gravida sit amet risus vehicular. Lorem ipsum dolor sit amet, consectetur adipiscing elit. Vivamus eu dui ex.</div>
  <svg class="footer-bar" viewBox="0 0 540 30"><rect x="0" y="26" width="540" height="4" fill="var(--sky)"/><polygon points="0,8 82,8 100,26 0,26" fill="var(--mist)"/><line x1="92" y1="18" x2="520" y2="18" stroke="var(--navy)" stroke-width="1.5"/><circle cx="520" cy="18" r="6" fill="var(--navy)"/><text x="520" y="20.5" font-size="6" fill="#fff" text-anchor="middle" font-family="Montserrat, Arial, sans-serif">3</text></svg>
  <div class="footer-brand">HALCYON</div>
</div>

<!-- row 5 -->
<div class="slide" style="left:50px;top:2153px">
  <div class="slide-title">Slide Title Goes Here</div>
  <div class="slide-sub">Subtitle of Slide Goes Here</div>
  <div role="img" aria-label="Photo of hands holding a tablet showing a stock chart" style="left:26px;top:92px;width:240px;height:158px;background:linear-gradient(135deg,#d7dce2,#4d5966)"></div>
  <div class="h-blue" style="left:282px;top:92px">Title Goes Here</div>
  <ul class="bul lorem" style="left:282px;top:110px;width:230px">
    <li>Lorem ipsum dolor sit amet, consectetur adipiscing elit. Vivamus eu dui ex. Curabitur dapibus dignissim dui, in molestie metus feugiat sed.</li>
    <li>Praesent aliquet lorem ex, eu dapibus odio varius at. Duis eget tellus porta, consequat lacus vitae, venenatis dolor.</li>
    <li>Nulla facilisi. In et sollicitudin lacus. Donec risus orci, gravida sit amet risus vehicula, aliquet pretium sapien. Nullam sit amet magna non ex bibendum mollis.</li>
    <li>Nunc vel neque eu augue dignissim congue ut vitae magna. Phasellus eget commodo arcu.</li>
    <li>Nunc vitae semper dui. Integer venenatis, tellus sit amet interdum pretium.</li>
  </ul>
  <svg class="footer-bar" viewBox="0 0 540 30"><rect x="0" y="26" width="540" height="4" fill="var(--sky)"/><polygon points="0,8 82,8 100,26 0,26" fill="var(--mist)"/><line x1="92" y1="18" x2="520" y2="18" stroke="var(--navy)" stroke-width="1.5"/><circle cx="520" cy="18" r="6" fill="var(--navy)"/><text x="520" y="20.5" font-size="6" fill="#fff" text-anchor="middle" font-family="Montserrat, Arial, sans-serif">4</text></svg>
  <div class="footer-brand">HALCYON</div>
</div>
<div class="slide" style="left:609px;top:2153px">
  <div class="slide-title">Slide Title Goes Here</div>
  <div class="slide-sub">Subtitle of Slide Goes Here</div>
  <div role="img" aria-label="Photo of people working on a laptop" style="left:24px;top:90px;width:157px;height:75px;background:linear-gradient(135deg,#dfe4ea,#3c4b5c)"></div>
  <div role="img" aria-label="Photo of laptop with financial dashboard" style="left:191px;top:90px;width:157px;height:75px;background:linear-gradient(135deg,#e6e9ed,#56636f)"></div>
  <div role="img" aria-label="Photo of coffee and tablet with charts" style="left:358px;top:90px;width:157px;height:75px;background:linear-gradient(135deg,#8a6b4c,#e6d6c1)"></div>
  <div class="h-blue" style="left:29px;top:172px;font-size:11px">Title Goes Here</div>
  <div class="h-blue" style="left:199px;top:172px;font-size:11px">Title Goes Here</div>
  <div class="h-blue" style="left:361px;top:172px;font-size:11px">Title Goes Here</div>
  <ul class="bul lorem" style="left:29px;top:188px;width:150px;font-size:6px"><li>Lorem ipsum dolor sit amet, consectetur adipiscing elit. Vivamus eu dui ex.</li><li>Curabitur dapibus dignissim dui, in molestie metus feugiat sed.</li><li>Praesent aliquet lorem ex, eu dapibus odio varius at.</li></ul>
  <ul class="bul lorem" style="left:199px;top:188px;width:150px;font-size:6px"><li>Lorem ipsum dolor sit amet, consectetur adipiscing elit. Vivamus eu dui ex.</li><li>Curabitur dapibus dignissim dui, in molestie metus feugiat sed.</li><li>Praesent aliquet lorem ex, eu dapibus odio varius at.</li></ul>
  <ul class="bul lorem" style="left:361px;top:188px;width:150px;font-size:6px"><li>Lorem ipsum dolor sit amet, consectetur adipiscing elit. Vivamus eu dui ex.</li><li>Curabitur dapibus dignissim dui, in molestie metus feugiat sed.</li><li>Praesent aliquet lorem ex, eu dapibus odio varius at.</li></ul>
  <svg class="footer-bar" viewBox="0 0 540 30"><rect x="0" y="26" width="540" height="4" fill="var(--sky)"/><polygon points="0,8 82,8 100,26 0,26" fill="var(--mist)"/><line x1="92" y1="18" x2="520" y2="18" stroke="var(--navy)" stroke-width="1.5"/><circle cx="520" cy="18" r="6" fill="var(--navy)"/><text x="520" y="20.5" font-size="6" fill="#fff" text-anchor="middle" font-family="Montserrat, Arial, sans-serif">5</text></svg>
  <div class="footer-brand">HALCYON</div>
</div>

<!-- row 6 -->
<div class="slide" style="left:50px;top:2475px;background:var(--sky)">
  <svg style="left:0;top:0;width:540px;height:302px" viewBox="0 0 540 302"><rect width="540" height="302" fill="url(#g-sectionbg)" role="img" aria-label="Faded photo of hands reviewing documents"/><circle cx="520" cy="128" r="190" fill="var(--navy)"/><circle cx="556" cy="118" r="176" fill="#8fb8dd"/></svg>
  <div class="brand" style="left:46px;top:72px"><span class="brand-sup">PROJECT</span><span class="brand-name" style="font-size:22px"><span class="brand-dot"></span>HALCYON</span></div>
  <div style="left:46px;top:150px;font-size:25px;font-weight:600;line-height:1.12;color:var(--white)">Section Break<br>Goes Here!</div>
  <div style="left:46px;top:214px;font-size:11px;color:var(--navy)">Subtitle of Section Break</div>
</div>
<div class="slide" style="left:609px;top:2475px">
  <div class="slide-title">Slide Title Goes Here</div>
  <div class="slide-sub">Subtitle of Slide Goes Here</div>
  <svg style="left:40px;top:92px;width:240px;height:160px" viewBox="0 0 240 160" font-family="Montserrat, Arial, sans-serif">
    <g font-size="5" fill="#777" text-anchor="end"><text x="8" y="7">6</text><text x="8" y="28">5</text><text x="8" y="49">4</text><text x="8" y="70">3</text><text x="8" y="91">2</text><text x="8" y="112">1</text><text x="8" y="133">0</text></g>
    <line x1="14" y1="131" x2="236" y2="131" stroke="#ccc" stroke-width=".6"/>
    <g>
      <rect x="28" y="77" width="10" height="54" fill="var(--navy)"/><rect x="39" y="94" width="10" height="37" fill="var(--ocean)"/><rect x="50" y="98" width="10" height="33" fill="var(--sky)"/>
      <rect x="87" y="100" width="10" height="31" fill="var(--navy)"/><rect x="98" y="73" width="10" height="58" fill="var(--ocean)"/><rect x="109" y="89" width="10" height="42" fill="var(--sky)"/>
      <rect x="146" y="85" width="10" height="46" fill="var(--navy)"/><rect x="157" y="96" width="10" height="35" fill="var(--ocean)"/><rect x="168" y="110" width="10" height="21" fill="var(--sky)"/>
      <rect x="205" y="71" width="10" height="60" fill="var(--navy)"/><rect x="216" y="85" width="10" height="46" fill="var(--ocean)"/><rect x="227" y="62" width="10" height="69" fill="var(--sky)"/>
    </g>
    <g font-size="5" fill="#777" text-anchor="middle"><text x="44" y="139">Category 1</text><text x="103" y="139">Category 2</text><text x="162" y="139">Category 3</text><text x="221" y="139">Category 4</text></g>
    <g font-size="4.5" fill="#777"><rect x="84" y="146" width="3" height="3" fill="var(--navy)"/><text x="89" y="149">Series 1</text><rect x="112" y="146" width="3" height="3" fill="var(--ocean)"/><text x="117" y="149">Series 2</text><rect x="140" y="146" width="3" height="3" fill="var(--sky)"/><text x="145" y="149">Series 3</text></g>
  </svg>
  <div class="legend" style="left:330px;top:96px;width:180px">
    <div class="legend-row" style="position:absolute;left:0;top:0"><span class="legend-sw" style="background:var(--navy)"></span><div class="h-blue" style="color:var(--navy)">Title Goes Here</div><div class="lorem" style="font-size:6px">Lorem ipsum dolor sit amet, consectetur adipiscing elit. Vivamus eu dui ex. Curabitur dapibus dignissim dui, in molestie metus.</div></div>
    <div class="legend-row" style="position:absolute;left:0;top:54px"><span class="legend-sw" style="background:var(--ocean)"></span><div class="h-blue">Title Goes Here</div><div class="lorem" style="font-size:6px">Lorem ipsum dolor sit amet, consectetur adipiscing elit. Vivamus eu dui ex. Curabitur dapibus dignissim dui, in molestie metus.</div></div>
    <div class="legend-row" style="position:absolute;left:0;top:108px"><span class="legend-sw" style="background:var(--sky)"></span><div class="h-blue" style="color:var(--sky)">Title Goes Here</div><div class="lorem" style="font-size:6px">Lorem ipsum dolor sit amet, consectetur adipiscing elit. Vivamus eu dui ex. Curabitur dapibus dignissim dui, in molestie metus.</div></div>
  </div>
  <svg class="footer-bar" viewBox="0 0 540 30"><rect x="0" y="26" width="540" height="4" fill="var(--sky)"/><polygon points="0,8 82,8 100,26 0,26" fill="var(--mist)"/><line x1="92" y1="18" x2="520" y2="18" stroke="var(--navy)" stroke-width="1.5"/><circle cx="520" cy="18" r="6" fill="var(--navy)"/><text x="520" y="20.5" font-size="6" fill="#fff" text-anchor="middle" font-family="Montserrat, Arial, sans-serif">6</text></svg>
  <div class="footer-brand">HALCYON</div>
</div>

<!-- row 7 -->
<div class="slide" style="left:50px;top:2796px">
  <div class="slide-title">Slide Title Goes Here</div>
  <div class="slide-sub">Subtitle of Slide Goes Here</div>
  <table class="grid" style="left:30px;top:82px">
    <tr><th>Koptekst</th><th>Koptekst</th><th>Koptekst</th><th>Koptekst</th></tr>
    <tr><td>Tekst komt hier</td><td>Tekst komt hier</td><td>Tekst komt hier</td><td>Tekst komt hier</td></tr>
    <tr><td>Tekst komt hier</td><td>Tekst komt hier</td><td>Tekst komt hier</td><td>Tekst komt hier</td></tr>
    <tr><td>Tekst komt hier</td><td>Tekst komt hier</td><td>Tekst komt hier</td><td>Tekst komt hier</td></tr>
    <tr><td>Tekst komt hier</td><td>Tekst komt hier</td><td>Tekst komt hier</td><td>Tekst komt hier</td></tr>
    <tr><td>Tekst komt hier</td><td>Tekst komt hier</td><td>Tekst komt hier</td><td>Tekst komt hier</td></tr>
    <tr><td>Tekst komt hier</td><td>Tekst komt hier</td><td>Tekst komt hier</td><td>Tekst komt hier</td></tr>
    <tr><td>Tekst komt hier</td><td>Tekst komt hier</td><td>Tekst komt hier</td><td>Tekst komt hier</td></tr>
    <tr><td>Tekst komt hier</td><td>Tekst komt hier</td><td>Tekst komt hier</td><td>Tekst komt hier</td></tr>
    <tr><td>Tekst komt hier</td><td>Tekst komt hier</td><td>Tekst komt hier</td><td>Tekst komt hier</td></tr>
  </table>
  <svg class="footer-bar" viewBox="0 0 540 30"><rect x="0" y="26" width="540" height="4" fill="var(--sky)"/><polygon points="0,8 82,8 100,26 0,26" fill="var(--mist)"/><line x1="92" y1="18" x2="520" y2="18" stroke="var(--navy)" stroke-width="1.5"/><circle cx="520" cy="18" r="6" fill="var(--navy)"/><text x="520" y="20.5" font-size="6" fill="#fff" text-anchor="middle" font-family="Montserrat, Arial, sans-serif">7</text></svg>
  <div class="footer-brand">HALCYON</div>
</div>
<div class="slide" style="left:609px;top:2796px;background:var(--ink)">
  <svg style="left:0;top:0;width:540px;height:282px" viewBox="0 0 540 282"><rect width="540" height="282" fill="url(#g-dark)" role="img" aria-label="Dark faded photo of a business handshake"/><circle cx="520" cy="128" r="190" fill="var(--navy)"/><circle cx="556" cy="118" r="176" fill="#16191e"/></svg>
  <div class="brand" style="left:46px;top:110px;color:var(--white)"><span class="brand-sup">PROJECT</span><span class="brand-name" style="font-size:22px"><span class="brand-dot"></span>HALCYON</span></div>
  <div style="left:46px;top:176px;font-size:12px;color:var(--white)">Contact Us</div>
  <div style="left:46px;top:196px;font-size:7px;color:var(--white);line-height:16px">
    <div><svg width="8" height="8" viewBox="0 0 24 24" style="vertical-align:-1px;margin-right:8px"><path fill="#fff" d="M6.6 10.8a15 15 0 0 0 6.6 6.6l2.2-2.2c.3-.3.7-.4 1-.2 1.1.4 2.3.6 3.6.6.6 0 1 .4 1 1V20c0 .6-.4 1-1 1A17 17 0 0 1 3 4c0-.6.4-1 1-1h3.5c.6 0 1 .4 1 1 0 1.3.2 2.5.6 3.6.1.3 0 .7-.2 1z"/></svg>555-0142-7788</div>
    <div><svg width="8" height="8" viewBox="0 0 24 24" style="vertical-align:-1px;margin-right:8px"><circle cx="12" cy="12" r="9" fill="none" stroke="#fff" stroke-width="2.5"/><circle cx="12" cy="12" r="3.5" fill="none" stroke="#fff" stroke-width="2.5"/></svg>info@project-halcyon.com</div>
    <div><svg width="8" height="8" viewBox="0 0 24 24" style="vertical-align:-1px;margin-right:8px"><circle cx="12" cy="12" r="9" fill="none" stroke="#fff" stroke-width="2"/><ellipse cx="12" cy="12" rx="4" ry="9" fill="none" stroke="#fff" stroke-width="2"/><line x1="3" y1="12" x2="21" y2="12" stroke="#fff" stroke-width="2"/></svg>www.project-halcyon.com</div>
  </div>
  <div style="left:0;bottom:0;width:540px;height:20px;background:var(--white);font-size:6px;display:flex;align-items:center;justify-content:center;color:#333">© 2020&nbsp;<b style="font-weight:500;color:var(--navy)">Project-Halcyon</b>&nbsp;| All Rights Reserved.</div>
</div>

</body>
</html>
```